Broschüre für eine Trainingsakademie
Zielgruppe
Ich möchte eine Broschüre zu meinem Unternehmen und meinen Angeboten schöner Design haben.
Ich bin Trainer/ Coach für moderne Personalstrategien insbesondere für die Personalgewinnung, Mitarbeiterbindung und -entwicklung. Zudem biete ich Trainings und Coachings für Mitarbeiter und Führungskräfte an. Zum Beispiel zu Themen wie gesunde Führung, Stressmanagement, Resilienz usw.
Meine Zielgruppe sind vor allem mittelständische Unternehmen oder junge aufstrebende StartUps, die ich beim Aufbau von Personalstrukturen unterstütze.
Aufgabenstellung
Mein Logo und die Farben sollen entsprechend berücksichtigt werden. Ein Entwurf für die Broschüre besteht bereits. Das ist allerdings nur meine Idee, als Laie. Ich hätte hier gern professionelle Ideen, so dass die Broschüre professionell und ansprechend wirkt.
Bilder habe ich eigentlich - diese finden sich auch auf meiner Homepage. Allerdings bin ich gerade auch beim Deckblatt offen. Auch für andere Gestaltungsvorschläge.

```html
<!DOCTYPE html>
<html lang="de">
<head>
<meta charset="utf-8">
<title>Trainingsakademie – Broschüre Deckblatt</title>
<link href="https://fonts.googleapis.com/css2?family=Arimo:wght@400;700&display=swap" rel="stylesheet">
<style>
  :root {
    --brand: #544a7d;
    --brand-soft: #a9a3bf;
    --ink: #1f1f24;
    --bar-top: #b4aec7;
    --bar-bottom: #958eac;
    --column-top: #a49cba;
    --column-bottom: #8f87aa;
    --chevron-light: #ebe9f3;
    --chevron-mid: #dedce6;
    --paper: #ffffff;
  }
  html, body {
    margin: 0;
    padding: 0;
    width: 1200px;
    height: 846px;
    overflow: hidden;
    background: var(--paper);
  }
  .cover {
    display: block;
    width: 1200px;
    height: 846px;
    font-family: "Arimo", Arial, sans-serif;
  }
  .brand-name { fill: var(--brand); font-weight: 700; font-size: 19px; letter-spacing: 1.5px; }
  .title-pre, .title-post { fill: var(--brand-soft); font-size: 31px; }
  .title-main { fill: var(--brand); font-size: 54px; }
  .topic { fill: var(--ink); font-size: 38px; }
  .topic .topic-key { font-weight: 700; }
  .rule { stroke: var(--brand); stroke-width: 2; fill: none; }
  .leader { stroke: var(--ink); stroke-width: 2; stroke-dasharray: 1.5 4; stroke-linecap: round; fill: none; }
  .chevron-light { fill: var(--chevron-light); }
  .chevron-mid { fill: var(--chevron-mid); }
</style>
</head>
<body>
<svg class="cover" viewBox="0 0 1200 846" xmlns="http://www.w3.org/2000/svg">
  <defs>
    <linearGradient id="barFill" x1="0" y1="0" x2="0" y2="1">
      <stop offset="0" stop-color="var(--bar-top)"/>
      <stop offset="1" stop-color="var(--bar-bottom)"/>
    </linearGradient>
    <linearGradient id="columnFill" x1="0" y1="0" x2="0" y2="1">
      <stop offset="0" stop-color="var(--column-top)"/>
      <stop offset="1" stop-color="var(--column-bottom)"/>
    </linearGradient>
    <linearGradient id="skylineFill" x1="0" y1="0" x2="0" y2="1">
      <stop offset="0" stop-color="#8f86a8"/>
      <stop offset="0.55" stop-color="#9fd3de"/>
      <stop offset="1" stop-color="#9c94b4"/>
    </linearGradient>
    <linearGradient id="figureFill" x1="0" y1="0" x2="0" y2="1">
      <stop offset="0" stop-color="#66597f"/>
      <stop offset="1" stop-color="#463c66"/>
    </linearGradient>
  </defs>

  <!-- background chevrons -->
  <g class="chevrons">
    <polygon class="chevron-light" points="0,0 62,0 265,222 145,339 22,339 142,220 0,78"/>
    <polygon class="chevron-mid" points="62,0 128,0 243,116 202,157"/>
    <polygon class="chevron-mid" points="0,75 112,186 48,250 0,205"/>
  </g>

  <!-- brand name -->
  <text class="brand-name" x="989" y="112" text-anchor="middle" textLength="240" lengthAdjust="spacingAndGlyphs">HALVORSEN COACHING</text>

  <!-- right image column -->
  <rect role="img" aria-label="Illustration: Geschäftsleute beim Sprintstart vor einer Stadtsilhouette" x="867" y="157" width="244" height="124" fill="url(#skylineFill)"/>
  <rect role="img" aria-label="Illustrationen: Sprung über Balkendiagramm, Team in Bewegung, Menschen auf verschlungenen Wegen" x="867" y="282" width="244" height="564" fill="url(#columnFill)"/>

  <!-- title frame -->
  <line class="rule" x1="128" y1="281" x2="867" y2="281"/>
  <line class="rule" x1="1111" y1="281" x2="1200" y2="281"/>
  <line class="rule" x1="0" y1="341" x2="716" y2="341"/>
  <line class="rule" x1="128" y1="281" x2="128" y2="363"/>
  <line class="rule" x1="716" y1="261" x2="716" y2="341"/>

  <text class="title-pre" x="73" y="307">die</text>
  <text class="title-main" x="133" y="332" textLength="578" lengthAdjust="spacingAndGlyphs">TRAININGSAKADEMIE</text>
  <text class="title-post" x="726" y="341">für</text>

  <!-- topics -->
  <text class="topic" x="502" y="422" text-anchor="end">PERSONAL<tspan class="topic-key">STRATEGIE</tspan></text>
  <text class="topic" x="502" y="495" text-anchor="end">PERSONAL<tspan class="topic-key">ENTWICKLUNG</tspan></text>
  <text class="topic" x="502" y="567" text-anchor="end">PERSONAL<tspan class="topic-key">FÜHRUNG</tspan></text>

  <!-- steps -->
  <rect x="494" y="814" width="34" height="32" fill="url(#barFill)"/>
  <rect x="545" y="774" width="43" height="72" fill="url(#barFill)"/>
  <rect x="605" y="643" width="90" height="203" fill="url(#barFill)"/>
  <rect x="712" y="460" width="136" height="386" fill="url(#barFill)"/>

  <!-- leaders -->
  <polyline class="leader" points="505,420 716,420 716,462"/>
  <polyline class="leader" points="505,493 610,493 610,648"/>
  <polyline class="leader" points="505,566 549,566 549,777"/>

  <!-- climbing figure -->
  <rect role="img" aria-label="Piktogramm: Person steigt eine Stufe hinauf" x="482" y="643" width="91" height="171" rx="8" fill="url(#figureFill)" opacity="0.9"/>
</svg>
</body>
</html>
```